Mother's Day Sale Banner Ad For Jewelry Site

We are looking for a designer to design a banner on our website advertising our Mother's Day Sale. I have enclosed a few pieces of jewelry we would like used in the ad. The ad size needs to be 1187 × 400. The ad should say:

Mother's Day Sale - Save 15% with Promo Code: LOVEMOM

Industry/Entity Type

Jewelry

```html
<!DOCTYPE html>
<html lang="en">
<head>
<meta charset="utf-8">
<title>Mother's Day Sale Banner</title>
<link href="https://fonts.googleapis.com/css2?family=Pinyon+Script&family=Open+Sans:wght@700&display=swap" rel="stylesheet">
<style>
  :root {
    --page-bg: #cbcbcb;
    --banner-cream: #fbf1df;
    --banner-gold: #f1dcb2;
    --banner-white: #ffffff;
    --ribbon-red: #c8101c;
    --ribbon-bright: #ee2b2b;
    --ribbon-dark: #9e0a12;
    --ring-gold: #d9b27a;
    --ring-gold-light: #f3dfb8;
    --jewel-bg: #f4f3f1;
    --jewel-gold: #d9b15a;
    --promo-grey: #5e5e5e;
  }
  * { margin: 0; padding: 0; box-sizing: border-box; }
  html, body {
    width: 1200px; height: 1200px; overflow: hidden;
    background: var(--page-bg);
  }
  .banner {
    position: absolute;
    left: 120px; top: 438px;
    width: 950px; height: 320px;
    overflow: hidden;
    background: var(--banner-white);
  }
  .banner-pattern {
    position: absolute; inset: 0;
    background:
      radial-gradient(ellipse 55% 80% at 50% 30%, var(--banner-gold) 0%, var(--banner-cream) 55%, var(--banner-white) 100%);
  }
  .sale-ribbon {
    position: absolute;
    left: 192px; top: 24px;
    width: 574px; height: 74px;
  }
  .sale-title {
    position: absolute;
    left: 192px; top: 20px;
    width: 574px; height: 80px;
    text-align: center;
    font-family: "Pinyon Script", cursive;
    font-size: 54px;
    line-height: 80px;
    color: var(--banner-white);
    white-space: nowrap;
  }
  .product-row {
    position: absolute; inset: 0;
  }
  .product-frame {
    position: absolute;
    top: 139px;
    width: 124px; height: 124px;
    border-radius: 50%;
    padding: 4px;
    background: linear-gradient(160deg, var(--ring-gold-light), var(--ring-gold) 50%, var(--ring-gold-light));
    box-shadow: 0 2px 4px rgba(120, 80, 30, 0.25);
  }
  .product-photo {
    width: 100%; height: 100%;
    border-radius: 50%;
    background: radial-gradient(circle at 50% 50%, var(--jewel-gold) 0%, #e7d3a6 32%, var(--jewel-bg) 62%);
  }
  .product-photo--diamond-band { background: radial-gradient(circle, #e9e2cf 0%, #d8c08a 28%, var(--jewel-bg) 60%); }
  .product-photo--crab-brooch { background: radial-gradient(circle, #c2306a 0%, #d9b15a 30%, var(--jewel-bg) 62%); }
  .product-photo--coral-ring { background: radial-gradient(circle at 50% 40%, #e0634e 0%, #d9b15a 34%, var(--jewel-bg) 64%); }
  .promo-line {
    position: absolute;
    left: 0; right: 0; top: 292px;
    text-align: center;
    font-family: "Open Sans", sans-serif;
    font-weight: 700;
    font-size: 16px;
    color: var(--promo-grey);
  }
</style>
</head>
<body>
  <section class="banner">
    <div class="banner-pattern" role="img" aria-label="Soft cream and gold floral swirl background pattern"></div>

    <svg class="sale-ribbon" viewBox="0 0 574 74" aria-hidden="true">
      <defs>
        <linearGradient id="ribbonFill" x1="0" y1="0" x2="1" y2="0">
          <stop offset="0" stop-color="var(--ribbon-dark)"/>
          <stop offset="0.18" stop-color="var(--ribbon-red)"/>
          <stop offset="0.3" stop-color="var(--ribbon-bright)"/>
          <stop offset="0.5" stop-color="var(--ribbon-red)"/>
          <stop offset="0.75" stop-color="var(--ribbon-bright)"/>
          <stop offset="1" stop-color="var(--ribbon-dark)"/>
        </linearGradient>
      </defs>
      <polygon points="0,0 574,0 558,37 574,74 0,74 16,37" fill="url(#ribbonFill)"/>
      <polygon points="22,7 552,7 540,37 552,67 22,67 34,37" fill="none" stroke="#e8333a" stroke-width="1"/>
    </svg>
    <h1 class="sale-title">Mother's Day Sale</h1>

    <div class="product-row">
      <div class="product-frame" style="left:157px"><div class="product-photo" role="img" aria-label="Gold rope rings with diamond X motif"></div></div>
      <div class="product-frame" style="left:327px"><div class="product-photo product-photo--diamond-band" role="img" aria-label="Gold and diamond wide band ring"></div></div>
      <div class="product-frame" style="left:498px"><div class="product-photo product-photo--crab-brooch" role="img" aria-label="Gold crab brooch set with pink stones"></div></div>
      <div class="product-frame" style="left:668px"><div class="product-photo product-photo--coral-ring" role="img" aria-label="Gold ring topped with carved coral"></div></div>
    </div>

    <p class="promo-line">Save 15% with Promo Code: LOVEMOM</p>
  </section>
</body>
</html>
```